Webpage Design Layout for Thanksgiving/App Charity

Hi,

I am putting together a website called http://cloverbright.example with the intention of getting app developers to giveaway their usual thanksgiving discount to a charity rather than to the customer.

I am looking for a one page design (not coded) that will have;

1. A header and small description of the idea. For example;

"Cloverbright - Kindness That Counts"

Cloverbright is a movement that lets developers and users pass on the usual Thanksgiving discounts to people and communities who need it most. Buy your favourite apps from the links below and 40% of the price goes directly to charity"

2. A small section outlining the charity (not yet selected) with a link to learn more and a 'Play Video' button. I'd like to include a video of the charity.

3. A grid showing the available apps with an 'About' button and 'Buy Now' button

4. a FAQ underneath the apps

5. Some kind of prominent "Money raised" bar that will go near the top of the page

6. A footer section with contact info, mailing list sign up.

7. A countdown timer near the top that will countdown until the charity is over

8. A logo that would represent Apps + Thanksgiving

Obviously since this ties in with thanksgiving and apps I'd like to make it a fun turkey or thanksgiving themed page.

Please use Google Fonts and make sure to have the rights to any images used.

Target Market(s)

I want to appeal to every day phone and computer users. It should be a fun page but that also display credibility and confidence for purchasers/visitors.

Industry/Entity Type

Software

Number of Pages Required

1 page

Requirements
Must have
• Just a fun page that displays credibility and the importance of the idea

```html
<!DOCTYPE html>
<html lang="en">
<head>
<meta charset="utf-8">
<title>Cloverbright - Kindness That Counts</title>
<link href="https://fonts.googleapis.com/css2?family=Roboto:wght@400;500;700&family=Open+Sans:wght@400;600;700&display=swap" rel="stylesheet">
<style>
:root{
  --green:#0a8a3e;
  --green-bright:#0ea24a;
  --ink:#1c1c1c;
  --text:#3a3a3a;
  --muted:#5b5b5b;
  --dark-btn:#2f2f2f;
  --white:#ffffff;
  --band:#f1f1f1;
  --footer:#f4f4f4;
  --line:#dcdcdc;
}
*{box-sizing:border-box;margin:0;padding:0}
html,body{width:1200px;height:2941px;overflow:hidden}
body{position:relative;background:var(--white);font-family:"Open Sans",Arial,sans-serif;color:var(--text)}
.abs{position:absolute}

/* header */
.site-header{position:absolute;left:0;top:0;width:1200px;height:98px;background:var(--white);box-shadow:0 1px 4px rgba(0,0,0,.12);z-index:2}
.brand{position:absolute;left:98px;top:30px;display:flex;align-items:center;gap:10px;font-family:"Roboto",Arial,sans-serif;font-weight:700;font-size:30px;color:var(--green)}
.brand-dot{width:26px;height:26px;border-radius:50%;background:var(--green)}
.main-nav{position:absolute;right:100px;top:40px;display:flex;gap:34px;font-family:"Roboto",Arial,sans-serif;font-size:15px;letter-spacing:.5px;color:#222}

/* hero */
.hero{position:absolute;left:0;top:98px;width:1200px;height:584px;overflow:hidden}
.hero-photo{position:absolute;inset:0;background:radial-gradient(ellipse at 50% 60%,#5a4636 0%,#3b2e25 45%,#1f1a17 100%)}
.hero-shade{position:absolute;inset:0;background:rgba(0,0,0,.35)}
.countdown{position:absolute;top:110px;left:0;width:1200px;display:flex;justify-content:center;gap:14px}
.count-unit{width:82px;height:82px;border-radius:50%;border:3px solid rgba(255,255,255,.85);color:var(--white);text-align:center;font-family:"Roboto",Arial,sans-serif;display:flex;flex-direction:column;justify-content:center;position:relative}
.count-unit::before{content:"";position:absolute;inset:-7px;border-radius:50%;border:3px solid transparent;border-top-color:#2aa7e0;border-right-color:#8c4fd0;border-bottom-color:#d94f8a}
.count-unit b{font-size:32px;font-weight:500;line-height:1}
.count-unit.small b{font-size:20px}
.count-unit span{font-size:10px;margin-top:2px}
.hero-title{position:absolute;top:312px;width:1200px;text-align:center;font-family:"Roboto",Arial,sans-serif;font-weight:700;font-size:38px;color:var(--white)}
.hero-sub{position:absolute;top:370px;width:1200px;text-align:center;font-family:"Roboto",Arial,sans-serif;font-size:19px;color:var(--white)}
.hero-text{position:absolute;top:408px;left:190px;width:820px;text-align:center;font-size:13.5px;line-height:24px;color:var(--white)}
.raise-bar{position:absolute;top:392px;left:363px;width:476px;height:12px;border-radius:6px;background:var(--white);overflow:hidden}
.raise-fill{width:51%;height:100%;background:var(--green)}
.raise-label{position:absolute;top:424px;font-size:15px;color:var(--white)}

/* charity */
.section-title{position:absolute;width:1200px;text-align:center;font-family:"Roboto",Arial,sans-serif;color:var(--ink)}
.charity-title{top:738px;font-size:40px;font-weight:500}
.charity-sub{top:798px;font-size:15px}
.video{position:absolute;left:98px;top:862px;width:1002px;height:441px;background:linear-gradient(135deg,#6b4a30 0%,#8a6a4a 45%,#c9b79c 70%,#5b3d26 100%)}
.play{position:absolute;left:460px;top:198px;width:82px;height:46px;border-radius:6px;background:rgba(240,240,240,.9)}
.btn{position:absolute;display:flex;align-items:center;justify-content:center;font-family:"Open Sans",Arial,sans-serif;font-weight:700;color:var(--white);border-radius:3px}
.learn-main{left:533px;top:1346px;width:134px;height:36px;background:var(--green);font-size:14px}

/* apps */
.apps{position:absolute;left:0;top:1450px;width:1200px;height:694px;background:var(--band)}
.apps-title{top:58px;font-size:34px;font-weight:500}
.rule{position:absolute;left:569px;width:62px;height:3px;background:var(--green)}
.app-card{position:absolute;width:476px;height:194px;border:2px solid var(--line);border-radius:97px;background:var(--white)}
.app-img{position:absolute;left:8px;top:9px;width:172px;height:172px;border-radius:50%}
.app-desc{position:absolute;left:206px;top:24px;width:240px;font-size:15px;line-height:25px;color:var(--text)}
.app-card .btn{top:143px;height:28px;font-size:11px;font-weight:600;border-radius:14px}
.btn-learn{left:204px;width:96px;background:var(--green-bright)}
.btn-buy{left:312px;width:98px;background:var(--dark-btn)}

/* faq */
.faq-title{top:2230px;font-size:34px;font-weight:500}
.faq-q{position:absolute;width:1200px;text-align:center;font-family:"Roboto",Arial,sans-serif;font-size:17px;color:var(--green)}
.faq-a{position:absolute;width:1200px;text-align:center;font-size:13px;color:var(--ink)}

/* footer */
.site-footer{position:absolute;left:0;top:2558px;width:1200px;height:265px;background:var(--footer);border-top:1px solid #e6e6e6}
.footer-heading{position:absolute;font-family:"Roboto",Arial,sans-serif;font-size:19px;color:var(--ink);letter-spacing:.3px}
.contact-item{position:absolute;left:98px;display:flex;gap:14px;font-size:13px;line-height:20px;color:var(--text)}
.contact-item svg{flex:none;margin-top:3px}
.footer-brand{position:absolute;left:0;top:110px;width:1200px;display:flex;justify-content:center;align-items:center;gap:12px;font-family:"Roboto",Arial,sans-serif;font-weight:700;font-size:40px;color:var(--green)}
.footer-brand .brand-dot{width:36px;height:36px}
.news-text{position:absolute;right:98px;top:100px;width:310px;text-align:right;font-size:12px;line-height:22px;color:var(--muted)}
.news-form{position:absolute;left:798px;top:158px;display:flex}
.news-input{width:204px;height:40px;border:1px solid #ddd;background:var(--white);font-size:11px;color:#666;padding:12px 14px}
.news-btn{width:98px;height:40px;background:var(--green);color:var(--white);font-weight:700;font-size:15px;display:flex;align-items:center;justify-content:center}
.bottom-bar{position:absolute;left:0;top:2823px;width:1200px;height:118px;border-top:1px solid #e0e0e0;text-align:center;font-size:11px;color:#333}
.bottom-links{position:absolute;top:38px;width:1200px}
.copyright{position:absolute;top:68px;width:1200px}
</style>
</head>
<body>

<header class="site-header">
  <div class="brand"><span class="brand-dot"></span>Cloverbright</div>
  <nav class="main-nav"><span>ABOUT</span><span>CHARITY</span><span>APPS</span><span>FAQ</span><span>CONTACT</span></nav>
</header>

<section class="hero">
  <div class="hero-photo" role="img" aria-label="Photo of a family gathered around a Thanksgiving dinner table"></div>
  <div class="hero-shade"></div>
  <div class="countdown">
    <div class="count-unit"><b>17</b><span>months</span></div>
    <div class="count-unit"><b>05</b><span>weeks</span></div>
    <div class="count-unit"><b>38</b><span>day</span></div>
    <div class="count-unit"><b>17</b><span>minutes</span></div>
    <div class="count-unit small"><b>00.15</b><span>seconds</span></div>
  </div>
  <h1 class="hero-title">CLOVERBRIGHT: KINDNESS THAT COUNTS</h1>
  <p class="hero-sub">40% OF ALL PURCHASES GOES TO CHARITY</p>
  <p class="hero-text" style="top:408px">Cloverbright is a movement that lets developers and users pass on the usual Thanksgiving discounts to people and communities who need it most. Buy your favourite apps from the links below and 40% of the price goes directly to charity*</p>
  <div class="raise-bar" style="top:486px"><div class="raise-fill"></div></div>
  <span class="raise-label" style="left:363px;top:424px;top:424px;margin-top:0;position:absolute;top:424px;top:424px;top:424px;top:424px;top:424px;top:424px;top:424px;top:424px;top:424px;top:424px;top:424px;top:426px;top:427px;top:428px;top:429px;top:430px;top:431px;top:432px;top:433px;top:434px;top:435px;top:436px;top:437px;top:438px;top:439px;top:440px;top:441px;top:442px;top:443px;top:444px;top:445px;top:446px;top:447px;top:448px;top:449px;top:450px;top:451px;top:452px;top:453px;top:454px;top:455px;top:456px;top:457px;top:458px;top:459px;top:460px;top:461px;top:462px;top:463px;top:464px;top:465px;top:466px;top:467px;top:468px;top:469px;top:470px;top:471px;top:472px;top:473px;top:474px;top:475px;top:476px;top:477px;top:478px;top:479px;top:480px;top:481px;top:482px;top:483px;top:484px;top:485px;top:486px;top:487px;top:488px;top:489px;top:490px;top:491px;top:492px;top:493px;top:494px;top:495px;top:496px;top:497px;top:498px;top:499px;top:500px;top:501px;top:502px;top:503px;top:504px;top:505px;top:506px;top:507px;top:508px;top:509px;top:510px;top:511px;top:512px;top:513px;top:514px;top:515px;top:516px;top:517px;top:518px;top:519px;top:520px;top:521px;top:522px;top:523px;top:524px">Money Raised: $100.00</span>
  <span class="raise-label" style="left:798px;top:524px">Goal</span>
</section>

<section>
  <h2 class="section-title charity-title">Charity Cloverbright</h2>
  <p class="section-title charity-sub">Charity Cloverbright helps children develop the skills they need</p>
  <div class="video" role="img" aria-label="Video still of a wooden desk with glasses, a coffee cup and a notebook sketched with the words give, help and charity">
    <svg class="play" viewBox="0 0 82 46" aria-hidden="true"><rect width="82" height="46" rx="6" fill="#eeeeee"/><path d="M34 13 L52 23 L34 33 Z" fill="#222"/></svg>
  </div>
  <a class="btn learn-main">LEARN MORE</a>
</section>

<section class="apps">
  <h2 class="section-title apps-title">AVAILABLE APPS</h2>
  <div class="rule" style="top:120px"></div>

  <article class="app-card" style="left:98px;top:181px">
    <div class="app-img" role="img" aria-label="Photo of a hand holding a phone with app icons flying out" style="background:radial-gradient(circle at 60% 40%,#3f8fd0,#1d3d5c 70%)"></div>
    <p class="app-desc">PageCraft is an easy to use website builder for DeskOS. The visual website builder is easy to use....</p>
    <a class="btn btn-learn">Learn More</a><a class="btn btn-buy">Buy Now</a>
  </article>
  <article class="app-card" style="left:623px;top:181px">
    <div class="app-img" role="img" aria-label="Illustration of a phone surrounded by app icons on a yellow background" style="background:radial-gradient(circle,#f6d23a,#f0b91a 70%)"></div>
    <p class="app-desc">PageCraft is an easy to use website builder for DeskOS. The visual website builder is easy to use....</p>
    <a class="btn btn-learn">Learn More</a><a class="btn btn-buy">Buy Now</a>
  </article>
  <article class="app-card" style="left:98px;top:422px">
    <div class="app-img" role="img" aria-label="Photo of hands holding a tablet with colourful app tiles" style="background:radial-gradient(circle at 50% 60%,#8a7fb8,#c9c2d8 75%)"></div>
    <p class="app-desc">PageCraft is an easy to use website builder for DeskOS. The visual website builder is easy to use....</p>
    <a class="btn btn-learn">Learn More</a><a class="btn btn-buy">Buy Now</a>
  </article>
  <article class="app-card" style="left:623px;top:422px">
    <div class="app-img" role="img" aria-label="Photo of hands holding a phone under a cloud of app icons" style="background:radial-gradient(circle,#8a6a5a,#4b3b36 75%)"></div>
    <p class="app-desc">PageCraft is an easy to use website builder for DeskOS. The visual website builder is easy to use....</p>
    <a class="btn btn-learn">Learn More</a><a class="btn btn-buy">Buy Now</a>
  </article>
</section>

<section>
  <h2 class="section-title faq-title">FAQS</h2>
  <div class="rule" style="top:2287px"></div>
  <h3 class="faq-q" style="top:2334px">HOW MUCH MONEY GOES CHARITY?</h3>
  <p class="faq-a" style="top:2366px">40% off all purchases that go through the Buy Now button for each app goes to charity</p>
  <h3 class="faq-q" style="top:2420px">WHAT CHARITY WILL THE MONEY GO TO?</h3>
  <p class="faq-a" style="top:2452px">40% off all purchases that go through the Buy Now button for each app goes to charity</p>
</section>

<footer class="site-footer">
  <h4 class="footer-heading" style="left:98px;top:68px">CONTACT US</h4>
  <div class="contact-item" style="top:108px">
    <svg width="12" height="16" viewBox="0 0 12 16"><path d="M6 0a6 6 0 0 0-6 6c0 4.5 6 10 6 10s6-5.5 6-10a6 6 0 0 0-6-6zm0 8.5A2.5 2.5 0 1 1 6 3.5a2.5 2.5 0 0 1 0 5z" fill="#333"/></svg>
    <span>Cloverbright Way, Suite 300 Maple<br>Falls CA 90000</span>
  </div>
  <div class="contact-item" style="top:162px">
    <svg width="14" height="14" viewBox="0 0 14 14"><path d="M3 0l2.5 3-1.5 2c1 2 2.5 3.5 4.5 4.5l2-1.5 3 2.5-1.5 2.5C6 13 1 8 .5 1.5z" fill="#333"/></svg>
    <span>Phone: (555) 010-4778</span>
  </div>
  <div class="contact-item" style="top:194px">
    <svg width="14" height="12" viewBox="0 0 14 12"><path d="M0 1h14v10H0z" fill="#333"/><path d="M0 1l7 5 7-5" stroke="#f4f4f4" stroke-width="1.4" fill="none"/></svg>
    <span>Email: info@cloverbright.example</span>
  </div>
  <div class="footer-brand"><span class="brand-dot"></span>Cloverbright</div>
  <h4 class="footer-heading" style="right:98px;top:62px">SIGN UP FOR NEWSLETTER</h4>
  <p class="news-text">Excepteur sint occaecat cupidatat non proident, sunt in culpa qui officia deserunt</p>
  <div class="news-form"><div class="news-input">Enter email</div><div class="news-btn">SIGN UP</div></div>
</footer>

<div class="bottom-bar">
  <p class="bottom-links">Home &nbsp;|&nbsp; About &nbsp;|&nbsp; Charity &nbsp;|&nbsp; Apps &nbsp;|&nbsp; FAQ &nbsp;|&nbsp; Contact</p>
  <p class="copyright">©2017 Cloverbright. All Rights Reserved.</p>
</div>

</body>
</html>
```